Poster for List of Company Values

We need a poster to outline our Values which will be displayed in our office as well as posted on our website and other platforms (so need to allow for some flexibly in its application).

File attached outlines what we currently have with design and also our company style guide.

Note that we are looking for a modern, clean look, which still represents our core activities of construction and environmental services.

You can also reference our website here:

https://quorvelgroup.com.au/

Happy to answer any questions you might have.

Thanks for your interest,
Brent

Target Market(s)

Internal and External clients

Industry/Entity Type

Construction, water and recycling

Font styles to use
Sans Serif

Requirements
Must have
• All values on the one page. Graphic to represent each value. Also needs to use company logo
Nice to have
• Preference for poster to be orientated in landscape
Should not have
• Do not follow example provided, this is only to demonstrate what we have to date and also the text required

```html
<!DOCTYPE html>
<html lang="en">
<head>
<meta charset="utf-8">
<title>Our Company Values – Quorvel Group</title>
<link href="https://fonts.googleapis.com/css2?family=Open+Sans:wght@400;600;700;800&display=swap" rel="stylesheet">
<style>
  :root {
    --navy: #0b3a8c;
    --green: #45ad3f;
    --paper: #eceeef;
    --paper-light: #f5f6f6;
    --ink: #2f3033;
    --white: #ffffff;
  }
  * { box-sizing: border-box; margin: 0; padding: 0; }
  html, body {
    width: 839px; height: 1200px; overflow: hidden;
    background: var(--white);
    font-family: "Open Sans", sans-serif;
  }
  .poster {
    position: absolute; left: 20px; top: 318px;
    width: 800px; height: 565px;
    background: linear-gradient(135deg, var(--paper-light) 0%, var(--paper) 45%, var(--paper-light) 100%);
    box-shadow: 0 10px 30px rgba(0,0,0,.28);
    overflow: hidden;
  }
  .brand {
    position: absolute; top: 34px; left: 0; width: 100%;
    display: flex; justify-content: center; align-items: center; gap: 12px;
  }
  .brand-dot { width: 34px; height: 34px; border-radius: 50%; background: var(--navy); }
  .brand-name {
    font-weight: 600; font-size: 22px; line-height: 1.05; color: var(--ink);
  }
  .title {
    position: absolute; top: 110px; width: 100%; text-align: center;
    font-size: 48px; font-weight: 400; color: var(--green); letter-spacing: -0.5px;
  }
  .title strong { font-weight: 800; color: var(--navy); }
  .band { position: absolute; top: 324px; height: 38px; }
  .band-green { left: 0; width: 400px; background: var(--green); }
  .band-navy { left: 400px; width: 400px; background: var(--navy); }

  .pill {
    position: absolute; width: 115px; height: 272px;
    border-radius: 58px; border: 2px solid;
    overflow: hidden; text-align: center; color: var(--white);
  }
  .pill-navy { background: var(--navy); border-color: var(--green); top: 217px; }
  .pill-green { background: var(--green); border-color: var(--navy); top: 172px; }
  .pill-icon {
    position: absolute; left: -2px; width: 115px; height: 115px;
    border-radius: 50%; background: var(--paper-light); border: 2px solid;
    display: flex; align-items: center; justify-content: center;
  }
  .pill-navy .pill-icon { bottom: -2px; border-color: var(--green); }
  .pill-green .pill-icon { top: -2px; border-color: var(--navy); }
  .icon-slot { width: 56px; height: 56px; border-radius: 50%; }
  .pill-navy .icon-slot { background: linear-gradient(135deg, var(--navy), var(--green)); }
  .pill-green .icon-slot { background: linear-gradient(135deg, var(--green), var(--navy)); }
  .pill-text { position: absolute; left: 8px; right: 8px; }
  .pill-navy .pill-text { top: 34px; }
  .pill-green .pill-text { top: 128px; }
  .value-name { font-weight: 700; font-size: 17px; line-height: 1.1; margin-bottom: 8px; }
  .value-desc { font-weight: 600; font-size: 8.4px; line-height: 1.4; }

  .web {
    position: absolute; top: 517px; width: 100%; text-align: center;
    font-weight: 700; font-size: 21px; letter-spacing: 4px; color: var(--navy);
  }
  .web span { color: var(--green); }
</style>
</head>
<body>
  <main class="poster">
    <header class="brand">
      <div class="brand-dot"></div>
      <div class="brand-name">QUORVEL<br>Group</div>
    </header>
    <h1 class="title">OUR COMPANY <strong>VALUES</strong></h1>

    <div class="band band-green"></div>
    <div class="band band-navy"></div>

    <section class="pill pill-navy" style="left:31px">
      <div class="pill-text">
        <h2 class="value-name">BE LOYAL</h2>
        <p class="value-desc">We take care of our own and provide opportunities to listenand support each other.</p>
      </div>
      <div class="pill-icon"><div class="icon-slot" role="img" aria-label="Icon of a team above a handshake"></div></div>
    </section>

    <section class="pill pill-green" style="left:153px">
      <div class="pill-icon"><div class="icon-slot" role="img" aria-label="Icon of a head with a light bulb and gear"></div></div>
      <div class="pill-text">
        <h2 class="value-name">SHOW<br>INITIATIVE</h2>
        <p class="value-desc">We celebrate and recognize our own and encourage forward thinking.</p>
      </div>
    </section>

    <section class="pill pill-navy" style="left:280px">
      <div class="pill-text">
        <h2 class="value-name">THINK<br>TEAM</h2>
        <p class="value-desc">We communicate effectively and work as a team by helping and supporting each other.</p>
      </div>
      <div class="pill-icon"><div class="icon-slot" role="img" aria-label="Icon of a group sharing an idea"></div></div>
    </section>

    <section class="pill pill-green" style="left:405px">
      <div class="pill-icon"><div class="icon-slot" role="img" aria-label="Icon of a handshake"></div></div>
      <div class="pill-text">
        <h2 class="value-name">SHOW<br>RESPECT</h2>
        <p class="value-desc">We value the diversity and opinions of all.</p>
      </div>
    </section>

    <section class="pill pill-navy" style="left:530px">
      <div class="pill-text">
        <h2 class="value-name">BE OPEN<br>AND<br>HONEST</h2>
        <p class="value-desc">We are clear and open with each other,and provide an approachable and friendly environment.</p>
      </div>
      <div class="pill-icon"><div class="icon-slot" role="img" aria-label="Icon of a hand holding a heart"></div></div>
    </section>

    <section class="pill pill-green" style="left:653px">
      <div class="pill-icon"><div class="icon-slot" role="img" aria-label="Icon representing positivity"></div></div>
      <div class="pill-text">
        <h2 class="value-name">BE<br>POSITIVE<br>AND SMILE</h2>
        <p class="value-desc">We are solutions focused and encourage a positive attitude turning a negative into a positive.</p>
      </div>
    </section>

    <footer class="web">www.<span>quorvelgroup</span>.com.au</footer>
  </main>
</body>
</html>
```